Label design for an exciting new Vodka brand

We need a label design for a dynamic new Vodka brand called 'Tall amber fern Vodka'. It is a crisp and versatile liquid with a clean and smooth finish. It should appeal to 21-39 year olds, with a slight female skew. Colours, fonts and styles should be modern and relatively neutral - take inspiration from the brand pictures attached.

Target Market(s)

21-39 year olds, both male and female, but with a slight female skew

```html
<!DOCTYPE html>
<html lang="en">
<head>
<meta charset="utf-8">
<title>Tall Amber Fern Vodka – Label</title>
<link rel="stylesheet" href="https://fonts.googleapis.com/css2?family=Prompt:wght@300;700&display=swap">
<style>
  :root {
    --navy: #23205c;
    --navy-soft: #2a2c6a;
    --teal-soft: #1e7a8c;
    --teal: #19aaa6;
    --gold: #d8b674;
    --gold-light: #fbedc8;
    --gold-deep: #d2ad6a;
    --white: #ffffff;
    --page: #ffffff;
  }
  * { margin: 0; padding: 0; box-sizing: border-box; }
  html, body {
    width: 1200px;
    height: 1000px;
    overflow: hidden;
    background: var(--page);
  }
  .canvas {
    position: relative;
    width: 1200px;
    height: 1000px;
  }
  .label {
    position: absolute;
    left: 250px;
    top: 34px;
    width: 700px;
    height: 933px;
    background: var(--navy);
    overflow: hidden;
    font-family: "Prompt", sans-serif;
    color: var(--white);
  }
  .wave-decoration {
    position: absolute;
    left: 0;
    right: 0;
    top: 490px;
    height: 130px;
    background: linear-gradient(100deg, var(--navy-soft) 0%, var(--navy-soft) 40%, var(--teal-soft) 80%, var(--teal) 100%);
    opacity: 0.85;
  }
  .brand-name {
    position: absolute;
    left: 0;
    right: 0;
    top: 92px;
    text-align: center;
    color: var(--gold);
    font-weight: 700;
    text-transform: uppercase;
    line-height: 1;
  }
  .brand-name .line-tall { display: block; font-size: 118px; letter-spacing: 0.02em; }
  .brand-name .line-amber { display: block; font-size: 128px; letter-spacing: 0.01em; margin-top: 6px; }
  .brand-name .line-fern { display: block; font-size: 58px; letter-spacing: 0.9em; margin-top: 26px; padding-left: 0.9em; }
  .product-type {
    position: absolute;
    left: 0;
    right: 0;
    top: 644px;
    text-align: center;
    font-size: 30px;
    font-weight: 300;
    letter-spacing: 1.35em;
    padding-left: 1.35em;
  }
  .product-copy {
    position: absolute;
    left: 80px;
    right: 80px;
    top: 735px;
    text-align: center;
    font-size: 24px;
    font-weight: 300;
    line-height: 35px;
  }
  .gold-band {
    position: absolute;
    left: 0;
    right: 0;
    bottom: 0;
    height: 26px;
    background: linear-gradient(90deg, var(--gold-deep) 0%, var(--gold-light) 48%, var(--gold-deep) 100%);
  }
</style>
</head>
<body>
<main class="canvas">
  <section class="label" aria-label="Tall Amber Fern Vodka bottle label">
    <div class="wave-decoration" role="img" aria-label="Decorative flowing teal and white wave lines sweeping across the label"></div>

    <h1 class="brand-name">
      <span class="line-tall">Tall</span>
      <span class="line-amber">Amber</span>
      <span class="line-fern">Fern</span>
    </h1>

    <p class="product-type">VODKA</p>

    <p class="product-copy">Lorem ipsum dolor sit amet, consectetuer adipiscing elit, sed diam nonummy nibh euismod tincidunt ut</p>

    <div class="gold-band"></div>
  </section>
</main>
</body>
</html>
```